Roofing Company Now Hiring and Call Now Facebook Ads

Trying to hire new sales reps in our Alabama market to add to our growing team. This is a great opportunity for any one looking for a career change or looking to add time back to the time they get to spend at home with their families. This is a chance to build a career in one of the fastest growing industries in the country and build financial freedom and a solid future for your family while easily making 6 figures yearly. Sales reps get to set their own schedule, take vacations when they want, and could even choose if they wanted to work in the summer or the winter seasons if they dont like the heat/cold environment. Sales reps are commission based with bonus/incentives for completing task and assignments weekly.

"Let's Talk About Your Roof!" Schedule a free Roof Inspection today!

Needing facebook ads for hiring and a few ads templates for daily post regarding roof inspections and roof replacements, if they are editable it would be easier for me to manage a few templates. This project needs to have a swag/cleanish look that attracts the younger group of people but still make the older group of customer think, man these guys have some solid looking things going on and looks like a well managed and built company. We also target the upper scale areas when seeking customers.

Lets see what yall got! lets Gooo!

Target Market(s)

Property owners, sales reps, homeowners, property managers, job seekers

Industry/Entity Type

Roofing Contractor Storm Restoration Contractor, Construction Contractor

Font styles to use
Sans Serif

Colors
EB3D1F
EC4F4E
F09395
F8D3D4
FCEDEE

Requirements
Must have
• Clean modern professional look with visible red and black colors, we like white too.
Nice to have
• red, black, white, popping eye catching colors.
Should not have
• wrong color red, red is more of a calder ridge otters red, please stay away from the pinkish red.

```html
<!DOCTYPE html>
<html lang="en">
<head>
<meta charset="utf-8">
<title>Ridgeline Roofing – We Are Hiring</title>
<link rel="stylesheet" href="https://fonts.googleapis.com/css2?family=Jost:wght@400;500;700&family=Archivo+Black&display=swap">
<style>
  :root {
    --red: #EB3D1F;
    --red-deep: #8f1f14;
    --red-mid: #b8321f;
    --charcoal: #1e1e20;
    --tile-dark: #2a2627;
    --white: #ffffff;
    --shirt: #f1efed;
  }
  * { margin: 0; padding: 0; box-sizing: border-box; }
  html, body { width: 1200px; height: 1070px; overflow: hidden; background: var(--charcoal); }
  .ad {
    position: relative;
    width: 1200px;
    height: 1070px;
    overflow: hidden;
    font-family: "Jost", sans-serif;
    color: var(--white);
  }
  .roof-backdrop {
    position: absolute; inset: 0;
    background:
      linear-gradient(180deg, rgba(30,28,29,0) 0%, rgba(30,28,29,0) 50%, rgba(160,45,30,0.9) 80%, var(--red-mid) 100%),
      linear-gradient(90deg, var(--tile-dark) 0%, #3a3031 40%, #6d2a22 70%, #c0361f 100%);
  }
  .bubble { position: absolute; left: 0; top: 0; }
  .megaphone {
    position: absolute; left: 0; top: 0; width: 300px; height: 260px;
  }
  .brand {
    position: absolute; left: 920px; top: 66px; width: 224px;
    text-align: center; font-weight: 700; color: var(--white);
    font-size: 30px; line-height: 1; letter-spacing: 1px;
  }
  .brand-sub { display: block; font-size: 15px; letter-spacing: 8px; margin-top: 8px; }
  .headline-small {
    position: absolute; left: 121px; top: 294px;
    font-size: 84px; font-weight: 500; line-height: 1; letter-spacing: 0;
  }
  .headline-big { position: absolute; left: 118px; top: 380px; }
  .headline-big text {
    font-family: "Archivo Black", sans-serif;
    fill: var(--red);
    stroke: var(--white);
    stroke-width: 5;
    paint-order: stroke;
  }
  .join-box {
    position: absolute; left: 112px; top: 600px; width: 554px; height: 118px;
    background: var(--charcoal);
    display: flex; align-items: center; justify-content: center;
    font-size: 58px; font-weight: 400; letter-spacing: 1px;
  }
  .join-box .accent { color: var(--red); margin-left: 16px; }
  .position-band {
    position: absolute; left: 53px; top: 866px; width: 700px; height: 125px;
    background: linear-gradient(90deg, #7a1a12 0%, rgba(160,40,28,0.6) 60%, rgba(180,50,30,0) 100%);
    display: flex; align-items: center; padding-left: 52px;
    font-size: 52px; font-weight: 400;
  }
  .position-band strong { font-weight: 700; margin-left: 20px; letter-spacing: 1px; }
  .portrait {
    position: absolute; left: 735px; top: 204px; width: 465px; height: 866px;
    background: linear-gradient(180deg, rgba(235,225,220,0) 0%, rgba(241,239,237,0.85) 35%, var(--shirt) 100%);
    border-radius: 240px 240px 0 0;
  }
</style>
</head>
<body>
  <main class="ad">
    <div class="roof-backdrop" role="img" aria-label="Dark roof tile texture fading into red"></div>

    <svg class="bubble" width="1200" height="1070" aria-hidden="true">
      <path d="M57 216 H750 V777 H660 L579 828 V777 H57 Z" fill="rgba(20,18,19,0.28)"/>
    </svg>

    <div class="megaphone" role="img" aria-label="White megaphone announcing the opening">
      <svg width="300" height="260" aria-hidden="true">
        <rect x="0" y="0" width="240" height="190" fill="#e9e9e9" opacity="0.9"/>
        <g stroke="#ffffff" stroke-width="5" stroke-linecap="round">
          <line x1="248" y1="80" x2="294" y2="88"/>
          <line x1="224" y1="130" x2="264" y2="150"/>
          <line x1="172" y1="184" x2="190" y2="224"/>
          <line x1="118" y1="204" x2="124" y2="250"/>
        </g>
      </svg>
    </div>

    <div class="brand">RIDGELINE<span class="brand-sub">ROOFING</span></div>

    <div class="portrait" role="img" aria-label="Smiling sales rep in a white shirt pointing at the headline"></div>

    <h1>
      <span class="headline-small">WE ARE</span>
      <svg class="headline-big" width="580" height="175" aria-label="Hiring">
        <text x="8" y="164" font-size="210" textLength="562" lengthAdjust="spacingAndGlyphs">HIRING</text>
      </svg>
    </h1>

    <div class="join-box">JOIN<span class="accent">OUR TEAM</span></div>

    <div class="position-band">POSITION:<strong>SALES REP</strong></div>
  </main>
</body>
</html>
```